Chiropractic healthcare group business card

We are a Portland Oregon based chiropractic healthcare group. Looking for a new business card design. Something cutting edge, that shows off our new logo and tag line.Use either of the attached logos.Our tag line = "Who would you be without pain?"I'm open to about anything, impress me!!
Target Market(s)
Chiropractic patients - Auto injury, back pain, sports injuries, neck , shoulder, hip, knee, ankle pain.
Industry/Entity Type
Chiropractic
Contact Information for Business Card
Dr. Bram Holtvick, D.C.
Clinic name - Fernway Chiropractic
2 clinics
location #1
20418 NW Marwick Road
Suite B
North Plains, OR 97133
Location #2
13529 SE Calloway Street
Portland OR 97236
Main phone line 971.555.0143
website : www.FernwayClinics.example
Tag line "Who would you be without pain?"
Colors
Designer to choose colors to be used in the design.
Requirements
Must have
- Use the logo colors -- Want the orange color to be a TRUE orange.
- Both clinic address
- phone number
- website
- personal email - b.holtvick@ReliefBeginsHere.example
- tag line - "Who would you be without pain?"

```html
<!DOCTYPE html>
<html lang="en">
<head>
<meta charset="utf-8">
<title>Fernway Chiropractic – Business Card</title>
<link rel="stylesheet" href="https://fonts.googleapis.com/css2?family=Open+Sans:wght@400;600;700;800&display=swap">
<style>
  :root {
    --orange: #f08a1c;
    --orange-deep: #e07d12;
    --gold: #f7b52b;
    --panel: #e9e9e9;
    --ink: #2d3a44;
    --white: #ffffff;
    --backdrop: #8a8a8a;
  }
  * { box-sizing: border-box; margin: 0; padding: 0; }
  html, body { width: 1200px; height: 862px; overflow: hidden; }
  body {
    background: var(--backdrop);
    font-family: "Open Sans", Arial, sans-serif;
    position: relative;
  }
  .card {
    position: absolute;
    width: 540px;
    height: 310px;
    background: var(--orange);
    overflow: hidden;
    box-shadow: 0 10px 24px rgba(0,0,0,0.35);
  }
  .card--front { left: 60px; top: 130px; }
  .card--back { left: 600px; top: 420px; }

  .front-website {
    position: absolute;
    right: 28px;
    bottom: 26px;
    color: var(--white);
    font-weight: 600;
    font-size: 19px;
    letter-spacing: 1px;
  }

  .back-shapes { position: absolute; inset: 0; }

  .brand {
    position: absolute;
    right: 26px;
    top: 40px;
    display: flex;
    align-items: center;
    gap: 8px;
    color: var(--ink);
    font-weight: 800;
    font-size: 15px;
    letter-spacing: 1.5px;
    text-transform: uppercase;
  }
  .brand-square { width: 14px; height: 14px; background: var(--orange); }

  .doctor-name {
    position: absolute;
    left: 26px;
    top: 108px;
    color: var(--white);
    font-weight: 800;
    font-size: 17px;
    letter-spacing: 0.5px;
    text-transform: uppercase;
  }
  .tagline {
    position: absolute;
    left: 26px;
    top: 132px;
    color: var(--ink);
    font-weight: 800;
    font-size: 9.5px;
    letter-spacing: 0.6px;
    text-transform: uppercase;
  }
  .tagline-rule {
    position: absolute;
    left: 26px;
    top: 150px;
    width: 210px;
    height: 2px;
    background: var(--gold);
  }
  .divider {
    position: absolute;
    left: 250px;
    top: 196px;
    width: 262px;
    height: 2px;
    background: var(--ink);
  }
  .address {
    position: absolute;
    display: flex;
    gap: 6px;
    color: var(--white);
    font-size: 9.5px;
    line-height: 1.35;
  }
  .address--north { left: 30px; top: 208px; }
  .address--south { left: 268px; top: 152px; }
  .pin { width: 10px; height: 14px; flex: none; margin-top: 1px; }
  .contact {
    position: absolute;
    left: 44px;
    top: 262px;
    color: var(--white);
    line-height: 1.4;
  }
  .contact-phone { font-size: 11px; font-weight: 600; }
  .contact-email { font-size: 9px; }
</style>
</head>
<body>

  <section class="card card--front" aria-label="Card front">
    <p class="front-website">www.FernwayClinics.example</p>
  </section>

  <section class="card card--back" aria-label="Card back">
    <svg class="back-shapes" width="540" height="310" viewBox="0 0 540 310" aria-hidden="true">
      <polygon points="200,0 232,0 540,206 540,228" fill="var(--gold)"/>
      <polygon points="214,0 222,0 540,212 540,220" fill="var(--orange-deep)"/>
      <polygon points="232,0 540,0 540,206" fill="var(--panel)"/>
    </svg>

    <div class="brand">
      <span class="brand-square"></span>
      <span>Fernway Chiropractic</span>
    </div>

    <h1 class="doctor-name">Dr. Bram Holtvick, D.C.</h1>
    <p class="tagline">Who would you be without pain?</p>
    <div class="tagline-rule"></div>

    <div class="address address--south">
      <svg class="pin" viewBox="0 0 10 14" aria-hidden="true"><path d="M5 0a4 4 0 0 1 4 4c0 3-4 10-4 10S1 7 1 4a4 4 0 0 1 4-4z" fill="var(--ink)"/><circle cx="5" cy="4" r="1.5" fill="var(--orange)"/></svg>
      <p>13529 SE Calloway Street<br>Portland OR 97236</p>
    </div>
    <div class="divider"></div>

    <div class="address address--north">
      <svg class="pin" viewBox="0 0 10 14" aria-hidden="true"><path d="M5 0a4 4 0 0 1 4 4c0 3-4 10-4 10S1 7 1 4a4 4 0 0 1 4-4z" fill="var(--ink)"/><circle cx="5" cy="4" r="1.5" fill="var(--orange)"/></svg>
      <p>20418 NW Marwick Road<br>Suite B<br>North Plains, OR 97133</p>
    </div>

    <div class="contact">
      <p class="contact-phone">Main phone line : 971.555.0143</p>
      <p class="contact-email">personal email: b.holtvick@ReliefBeginsHere.example</p>
    </div>
  </section>

</body>
</html>
```